Quenlorra, a Pet Sanitizer using a non alcohol product

It's a label for a Pet Sanitizer. I have attached my proposed concept.
It's going to be on a 500 mil plastic spray bottle. What I did is my idea I want to see yours. In the end, I want two versions, one label for a white spray bottle and one for a cobalt blue bottle The seal I used is only an example. I need it to stand out and transparent to the background.
The label needs to look safe, professional, current, and friendly.
My label looks a bit busy, dark, and not professional. please give me your ideas and concept. Thx,
Updates

"Quenlorra" is the company name. I have attached the company's logo herein. However, I believe that in today's market the logos are not important. Maybe you can make the water drop a watermark behind the company name. This is only a suggestion and I will wait to see your ideas. Thx,

Target Market(s)

Pet Owners

Industry/Entity Type

Pet Care

Font styles to use
Sans Serif

Requirements
Must have
• see upload file
Nice to have
• Professional
Should not have
• cartoons

```html
<!DOCTYPE html>
<html lang="en">
<head>
<meta charset="utf-8">
<title>Quenlorra Antimicrobial Pet Sanitizer Label</title>
<link href="https://fonts.googleapis.com/css2?family=Montserrat:wght@300;400;500;600&family=Oswald:wght@400;500;600&display=swap" rel="stylesheet">
<style>
  :root{
    --navy:#0f1d3d;
    --navy-soft:#7a8296;
    --sky:#3ab0e6;
    --blue:#1a78c2;
    --band:#2a93d6;
    --band-light:#6cc2ea;
    --ink:#23304f;
    --muted:#4b5674;
    --rule:#8b8f99;
    --seal:#7fb87a;
    --paper:#ffffff;
    --backdrop:#eef0f3;
  }
  *{margin:0;padding:0;box-sizing:border-box}
  html,body{width:1200px;height:1200px;overflow:hidden;background:var(--backdrop)}
  .label{
    position:absolute;left:160px;top:35px;width:880px;height:1130px;
    background:var(--paper);overflow:hidden;
    font-family:"Montserrat",sans-serif;color:var(--ink);
  }
  .brand-band{
    position:absolute;left:0;top:0;width:100%;height:194px;
    background:linear-gradient(90deg,var(--navy-soft) 0%,var(--navy) 30%,var(--navy) 70%,var(--navy-soft) 100%);
  }
  .brand-name{
    position:absolute;left:0;right:0;top:70px;text-align:center;
    font-weight:400;font-size:46px;letter-spacing:12px;color:var(--paper);
  }
  .origin-badge{
    position:absolute;left:509px;top:147px;width:124px;height:124px;border-radius:50%;
    background:var(--paper);border:3px solid var(--navy);box-shadow:0 0 0 5px var(--paper);
  }
  .claims{position:absolute;left:0;top:310px;width:100%;height:80px}
  .claim{
    position:absolute;top:0;width:80px;height:80px;border-radius:50%;
    border:2px dashed var(--muted);display:flex;flex-direction:column;
    align-items:center;justify-content:center;text-align:center;
    font-size:10px;font-weight:500;line-height:1.25;color:var(--muted);letter-spacing:.5px;
  }
  .claim svg{width:24px;height:24px;margin:2px 0}
  .headline{
    position:absolute;left:0;right:0;text-align:center;
    font-family:"Oswald",sans-serif;font-weight:500;line-height:1;
  }
  .headline-top{
    top:428px;font-size:104px;letter-spacing:1px;
    background:linear-gradient(90deg,var(--sky),var(--blue));
    -webkit-background-clip:text;background-clip:text;color:transparent;
  }
  .headline-main{top:528px;font-size:104px;color:var(--navy);letter-spacing:1px}
  .headline-main .light{color:var(--ink);font-weight:400}
  .tagline{
    position:absolute;left:0;right:0;top:660px;text-align:center;
    font-size:30px;font-weight:500;color:var(--muted);
  }
  .tagline span{
    color:var(--navy);font-weight:600;
    background:linear-gradient(90deg,rgba(42,147,214,.05),rgba(42,147,214,.45),rgba(42,147,214,.05));
    padding:2px 4px;
  }
  .efficacy{
    position:absolute;left:0;right:0;top:742px;text-align:center;
    font-size:30px;font-weight:500;line-height:42px;color:var(--navy);
  }
  .efficacy .second{display:block;color:var(--muted);padding-right:40px}
  .rule{position:absolute;left:208px;top:836px;width:440px;height:3px;background:var(--rule)}
  .pet-seal{
    position:absolute;left:634px;top:758px;width:134px;height:134px;border-radius:50%;
    border:4px solid var(--seal);background:rgba(127,184,122,.12);
  }
  .benefits{
    position:absolute;left:0;right:0;top:856px;text-align:center;
    font-size:32px;font-weight:500;color:var(--band);padding-right:40px;
  }
  .species-art{
    position:absolute;left:183px;top:922px;width:492px;height:90px;border-radius:8px;
    background:linear-gradient(90deg,#7f8aa6,#1f2d52);opacity:.85;
  }
  .volume-band{
    position:absolute;left:0;top:1018px;width:100%;height:74px;
    background:linear-gradient(var(--band) 0 14px,var(--band-light) 14px,var(--blue) 100%);
    display:flex;align-items:center;justify-content:center;padding-top:12px;
    font-size:32px;font-weight:500;color:var(--paper);
  }
</style>
</head>
<body>
<div class="label">
  <div class="brand-band">
    <div class="brand-name">QUENLORRA</div>
  </div>
  <div class="origin-badge" aria-hidden="true"></div>

  <div class="claims">
    <div class="claim" style="left:136px">NON<svg viewBox="0 0 24 24" fill="none" stroke="currentColor" stroke-width="1.5"><path d="M9 3h6M10 3v6l-5 10h14l-5-10V3"/></svg>TOXIC</div>
    <div class="claim" style="left:230px">ALCOHOL<svg viewBox="0 0 24 24" fill="none" stroke="currentColor" stroke-width="1.5"><path d="M12 3c4 5 6 8 6 11a6 6 0 0 1-12 0c0-3 2-6 6-11z"/><path d="M5 5l14 14"/></svg>FREE</div>
    <div class="claim" style="left:332px">NATURAL<svg viewBox="0 0 24 24" fill="none" stroke="currentColor" stroke-width="1.5"><path d="M12 21V9M12 9c-4-1-6-4-6-6 4 0 6 3 6 6zM12 12c4-1 6-4 6-6-4 0-6 3-6 6z"/></svg>PURE</div>
    <div class="claim" style="left:438px">HYPO-<svg viewBox="0 0 24 24" fill="none" stroke="currentColor" stroke-width="1.5"><circle cx="12" cy="12" r="8"/><path d="M8 12l3 3 5-6"/></svg>ALLERGENIC</div>
    <div class="claim" style="left:543px">NON-<svg viewBox="0 0 24 24" fill="none" stroke="currentColor" stroke-width="1.5"><rect x="7" y="9" width="10" height="12" rx="2"/><path d="M10 9V5h4v4M4 4l16 16"/></svg>SCENTED</div>
    <div class="claim" style="left:639px">VEGAN<svg viewBox="0 0 24 24" fill="none" stroke="currentColor" stroke-width="1.5"><path d="M12 20c-5-2-7-7-6-12 4 1 6 4 6 12zM12 20c5-2 7-7 6-12-4 1-6 4-6 12z"/></svg></div>
  </div>

  <div class="headline headline-top">ANTIMICROBIAL</div>
  <div class="headline headline-main"><span class="light">PET</span> SANITIZER</div>

  <div class="tagline">A SAFER <span>ALTERNATIVE TO ALCOHOL</span></div>

  <div class="efficacy">KILLS 99.9% of<span class="second">BACTERIA AND VIRUSES</span></div>
  <div class="rule"></div>
  <div class="pet-seal" aria-hidden="true"></div>

  <div class="benefits">Deodorizes - Desinfects</div>

  <div class="species-art" role="img" aria-label="Silhouettes of a dog, a cat, a horse and a rabbit"></div>

  <div class="volume-band">500 ml</div>
</div>
</body>
</html>
```